K&T Fixit and Rebuild general contracting business card design

I already have a logo that I want to use and I need a card that uses that logo and color scheme on the front with the address phone numbers and email and on the back a place for technicians to write in their name and phone number when they hand it out. It will need the License number of License #KTFXTRB318QN.
It should say General Contractor under the company name. The address is
4417 NE 3rd Ave, Ste D246
Vancouver, WA 98612
www.kandtfixitandrebuild.example
office@kandtfixitandrebuild.example
360-555-0182 is the telephone number
360-555-0149 is the fax number

Target Market(s)

Homeowners needing remodel work or repairs in their home.

Industry/Entity Type

Construction

Contact Information for Business Card

Business name, address, phone number, license number, fax number, email, and website on the front and a place to fill in technician's name and number

Font styles to use
Serif

Requirements
Must have
• Business name, address, phone number, license number, fax number, email, and website on the front and a place to fill in technician's name and number
Nice to have
• I uploaded an example of a front that is good.
Should not have
• Froo froo or extra embellishments.

```html
<!DOCTYPE html>
<html lang="en">
<head>
<meta charset="utf-8">
<title>K&amp;T Fixit and Rebuild – Business Card</title>
<link rel="stylesheet" href="https://fonts.googleapis.com/css2?family=Open+Sans:wght@400&display=swap">
<style>
  :root {
    --backdrop: #e3e3e3;
    --card-white: #f4f4f4;
    --wood-dark: #2a1510;
    --wood-mid: #4a281c;
    --copper: #c98a5c;
    --copper-deep: #a65d35;
    --strip-brown: #5b2f1e;
    --strip-dark: #1b0e0b;
    --ink: #2f2f2f;
  }
  * { margin: 0; padding: 0; box-sizing: border-box; }
  html, body { width: 1200px; height: 960px; overflow: hidden; }
  body {
    background: var(--backdrop);
    font-family: "Open Sans", Arial, sans-serif;
    position: relative;
  }
  .card {
    position: absolute;
    left: 305px;
    width: 592px;
    height: 337px;
    overflow: hidden;
  }
  /* Front */
  .card-front { top: 116px; }
  .wood-surface {
    position: absolute; inset: 0;
    background: radial-gradient(ellipse at 50% 45%, var(--wood-mid) 0%, var(--wood-dark) 100%);
  }
  .front-brand {
    position: absolute; left: 0; right: 0; top: 150px;
    text-align: center;
    font-size: 30px;
    line-height: 40px;
    color: var(--copper);
  }
  .front-tagline {
    position: absolute; left: 0; right: 0; top: 272px;
    text-align: center;
    font-size: 15px;
    line-height: 20px;
    color: var(--copper);
    letter-spacing: 2px;
    text-transform: uppercase;
  }
  /* Back */
  .card-back { top: 507px; background: var(--card-white); }
  .edge-strip { position: absolute; left: 0; top: 0; width: 13px; height: 100%; }
  .fill-in { position: absolute; left: 47px; top: 59px; }
  .fill-label { font-size: 16px; color: var(--copper-deep); line-height: 20px; }
  .fill-phone { display: block; margin-top: 8px; width: 10px; height: 14px; }
  .contact-block {
    position: absolute; left: 47px; top: 152px;
    font-size: 15.5px; line-height: 20px; color: var(--ink);
  }
  .contact-block address { font-style: normal; }
  .license-label { color: var(--copper-deep); }
  .contact-list { list-style: none; margin-top: 8px; }
  .contact-list li { display: flex; align-items: center; gap: 3px; }
  .contact-list svg { width: 13px; height: 13px; flex: none; fill: var(--copper-deep); }
  .back-brand {
    position: absolute; right: 30px; top: 128px;
    width: 170px;
    text-align: right;
    font-size: 22px; line-height: 30px;
    color: var(--copper-deep);
  }
</style>
</head>
<body>

<section class="card card-front" aria-label="Card front">
  <div class="wood-surface" role="img" aria-label="Dark stained wood plank background"></div>
  <p class="front-brand">K&amp;T Fixit and Rebuild</p>
  <p class="front-tagline">General Contractor</p>
</section>

<section class="card card-back" aria-label="Card back">
  <svg class="edge-strip" viewBox="0 0 13 337" preserveAspectRatio="none" aria-hidden="true">
    <rect x="0" y="0" width="13" height="337" fill="var(--strip-dark)"/>
    <polygon points="0,0 13,0 13,112 0,128" fill="var(--strip-brown)"/>
    <line x1="0" y1="131" x2="13" y2="115" stroke="#ffffff" stroke-width="2"/>
  </svg>

  <div class="fill-in">
    <p class="fill-label">Name</p>
    <svg class="fill-phone" viewBox="0 0 10 14" aria-label="Mobile phone">
      <rect x="1" y="0.8" width="8" height="12.4" rx="1.2" fill="none" stroke="var(--copper-deep)" stroke-width="1.4"/>
      <line x1="4" y1="11" x2="6" y2="11" stroke="var(--copper-deep)" stroke-width="1.2"/>
    </svg>
  </div>

  <div class="contact-block">
    <address>
      4417 NE 3rd Ave, Ste D246<br>
      Vancouver, WA 98612
    </address>
    <p><span class="license-label">License</span> #KTFXTRB318QN</p>
    <ul class="contact-list">
      <li>
        <svg viewBox="0 0 16 16" aria-label="Telephone"><path d="M3.6 1.5l2.4 2.9-1.4 1.6c.9 2 2.6 3.7 4.6 4.6l1.6-1.4 2.9 2.4-1.5 2.3C7 13.6 2.4 9 1.2 3z"/></svg>
        360-555-0182
      </li>
      <li>
        <svg viewBox="0 0 16 16" aria-label="Fax"><rect x="4" y="1.5" width="8" height="4"/><rect x="1" y="6" width="14" height="6" rx="1"/><rect x="4" y="10" width="8" height="4.5"/></svg>
        360-555-0149
      </li>
      <li>
        <svg viewBox="0 0 16 16" aria-label="Email"><path d="M1 3h14v10H1z M2.5 4.5v.4L8 9l5.5-4.1v-.4z" fill-rule="evenodd"/></svg>
        office@kandtfixitandrebuild.example
      </li>
      <li>
        <svg viewBox="0 0 16 16" aria-label="Website"><circle cx="8" cy="8" r="6.5" fill="none" stroke="var(--copper-deep)" stroke-width="1.4"/><path d="M1.5 8h13M8 1.5c-3 3.5-3 9.5 0 13M8 1.5c3 3.5 3 9.5 0 13" fill="none" stroke="var(--copper-deep)" stroke-width="1.1"/></svg>
        www.kandtfixitandrebuild.example
      </li>
    </ul>
  </div>

  <p class="back-brand">K&amp;T Fixit and Rebuild</p>
</section>

</body>
</html>
```